Webdesign für Maklerbüro
Zielgruppe
Wir sind ein Maklerbüro aus Nürnberg, das sich auf den Verkauf von Eigentumswohnungen und Häuser spezialisiert hat. Mit der neuen Seite möchten wir vor allem Eigentümer ansprechen und über unsere Arbeitsweise informieren. Der Hauptzweck ist damit die Akquise von neuen Objekten, für die Vermittlung. Die Zielgruppe sind vornehmlich Immobilienbesitzer im Alter 40+ und im gehobenen Preissegment.
Aufgabenstellung
Beim Design bitte an den Vorgaben des Logo (Datei beigefügt) orientieren. Bilder und Texte können durch 'Platzhalter' ersetzt werden.
Grundsätzlich stellt es für uns kein Problem dar, sich an Template-Vorlagen zu orientieren. Wir stellen uns eine Seite mit Pfiff und Ideenreichtum – einfach weg vom Standard – vor. Wir verkaufen Immobilien, aber vom verstaubten Krawattenträger sind wir weit entfernt. Wir sind ein junges Unternehmen, das neue Marketingwege beschreitet. Unsere Webseite muss das ausdrücken. Kein Standard, und damit auch keine Standard-Webseite. Designs, die uns gut gefallen (und in die Richtung es auch gehen kann) haben wir beigefügt.

```html
<!DOCTYPE html>
<html lang="de">
<head>
<meta charset="utf-8">
<title>Giebelhaus – Immobilienmakler Metropolregion Nürnberg</title>
<link rel="stylesheet" href="https://fonts.googleapis.com/css2?family=Open+Sans:wght@400;700&family=Ubuntu:wght@300;400;500&display=swap">
<style>
:root{
  --navy:#1b2340;
  --navy-soft:#232c4c;
  --page:#e1e1e1;
  --accent:#1b9ad6;
  --card-gray:#a9aab0;
  --card-gray-back:#b6b7bc;
  --white:#ffffff;
  --ink:#1b2340;
}
*{margin:0;padding:0;box-sizing:border-box}
html,body{width:1200px;height:3075px;overflow:hidden}
body{position:relative;background:var(--page);font-family:"Open Sans",Arial,sans-serif;color:var(--ink)}
.abs{position:absolute}

/* Hero */
.hero{left:0;top:0;width:1200px;height:537px;background:linear-gradient(180deg,#5e6a86 0%,#8a8a96 35%,#6d7480 60%,#4f5a52 85%,#5b6a4a 100%)}
.nav-bar{left:0;top:72px;width:1105px;height:53px;background:var(--navy)}
.brand{left:125px;top:82px;height:56px;display:flex;align-items:center;gap:12px;color:var(--white);font-family:"Open Sans",sans-serif;font-weight:400;font-size:28px;letter-spacing:1px}
.brand-mark{width:18px;height:18px;border:2px solid var(--white)}
.burger{left:1057px;top:84px;width:36px;height:28px}
.burger span{display:block;height:4px;background:var(--white);margin-bottom:8px}
.hero-title{left:0;top:250px;width:1200px;text-align:center;color:var(--white);font-weight:700;font-size:27px;text-shadow:0 1px 3px rgba(0,0,0,.4)}
.hero-btn{left:460px;top:392px;width:277px;height:49px;border:3px solid var(--accent);color:var(--white);font-weight:700;font-size:23px;display:flex;align-items:center;justify-content:center;background:rgba(27,35,64,.25)}

/* Intro */
.intro-shapes{left:0;top:537px;width:1200px;height:670px}
.intro-title{left:0;top:568px;width:1170px;text-align:center;font-family:"Ubuntu",sans-serif;font-weight:400;font-size:31px}
.intro-text{left:587px;top:642px;width:513px;font-size:22.5px;line-height:28.2px;text-align:justify;hyphens:auto}
.band-title{left:0;top:1096px;width:1200px;text-align:center;color:var(--white);font-weight:700;font-size:35px}

/* Services */
.services-title{left:0;top:1224px;width:1200px;text-align:center;font-family:"Ubuntu",sans-serif;font-size:31px}
.svc-icon-box{left:204px;top:1301px;width:194px;height:262px;background:var(--navy)}
.svc-back{left:497px;top:1301px;width:192px;height:262px;background:var(--card-gray-back)}
.svc-card{top:1319px;height:224px;padding:30px 22px 0 38px;font-family:"Ubuntu",sans-serif}
.svc-card h3{font-weight:400;font-size:25px;text-align:center;margin-bottom:18px}
.svc-card p{font-size:19px;line-height:24px}
.svc-card.active{left:398px;width:308px;background:var(--navy);color:var(--white)}
.svc-card.muted{left:706px;width:292px;background:var(--card-gray);color:#dcdde2;padding-left:22px}
.svc-card.muted h3{text-align:left;padding-left:26px}
.slider-arrow{top:1415px;width:36px;height:36px;border-radius:50%;background:var(--navy);color:var(--white);font-size:20px;display:flex;align-items:center;justify-content:center}

/* Key photo band */
.key-band{left:0;top:1618px;width:1200px;height:145px}

/* Testimonial */
.quote-title{left:278px;top:1814px;font-family:"Ubuntu",sans-serif;font-size:32px}
.quote-mark{left:114px;top:1915px}
.quote-text{left:252px;top:1939px;width:527px;font-family:"Ubuntu",sans-serif;font-weight:300;font-size:24.5px;line-height:28.2px;text-align:justify;color:#141a30}
.portrait{left:0;top:1810px;width:1200px;height:470px}

/* Contact */
.contact-bar{left:82px;top:2328px;width:1118px;height:54px;background:var(--navy)}
.contact-map{left:82px;top:2382px;width:1118px;height:145px}
.contact-title{left:0;top:2563px;width:1200px;text-align:center;font-family:"Ubuntu",sans-serif;font-size:31px}
.contact-item{left:110px;display:flex;align-items:center;gap:40px;font-size:15.5px;line-height:27px}
.contact-item svg{width:46px;flex:none}
.field{height:34px;background:var(--navy);border-right:5px solid var(--accent);color:var(--white);font-size:14.5px;padding:9px 16px}
.field.message{height:193px}

/* Footer */
.footer{left:0;top:3029px;width:1200px;height:46px;background:var(--navy);color:var(--white);font-size:16px}
.footer a{position:absolute;top:13px;color:var(--white);text-decoration:none}
</style>
</head>
<body>

<header>
  <div class="abs hero" role="img" aria-label="Foto eines Einfamilienhauses mit Doppelgarage in der Abenddämmerung"></div>
  <div class="abs nav-bar"></div>
  <div class="abs brand"><span class="brand-mark"></span>GIEBELHAUS</div>
  <div class="abs burger" aria-label="Menü"><span></span><span></span><span></span></div>
  <h1 class="abs hero-title">Ihr Immobilienmakler für die Metropolregion Nürnberg.</h1>
  <a class="abs hero-btn">Wer wir sind.</a>
</header>

<section>
  <svg class="abs intro-shapes" viewBox="0 537 1200 670" width="1200" height="670">
    <defs>
      <linearGradient id="villaTone" x1="0" y1="0" x2="1" y2="1">
        <stop offset="0" stop-color="#9fb6cf"/>
        <stop offset=".5" stop-color="#e8ecef"/>
        <stop offset="1" stop-color="#5f7246"/>
      </linearGradient>
    </defs>
    <polygon points="0,537 543,854 0,1165" fill="url(#villaTone)" role="img" aria-label="Foto einer modernen weißen Villa mit Glasfronten"/>
    <polygon points="0,1165 257,1060 1200,1060 1200,1188 599,1206 0,1168" fill="var(--navy)"/>
    <polygon points="579,1164 619,1164 599,1183" fill="var(--white)"/>
  </svg>
  <h2 class="abs intro-title">Die richtige Wahl des Immobilienmaklers.</h2>
  <p class="abs intro-text">Lorem ipsum dolor sit amet, consectetur adipiscing elit. Pellentesque varius commodo nulla eget placerat. Integer molestie lectus vitae eros maximus lobortis. Ut tincidunt sollicitudin felis, et ultrices sem tempus vitae. Maecenas euismod, enim eget gravida maximus, massa metus volutpat ante, id fermentum metus purus non mi. Morbi id metus sed purus finibus aliquet. Aliquam ac eros cursus, dapibus ex sed, elementum leo. Aliquam gravida feugiat ligula, a volutpat nulla fermentum non. Nam vitae nulla interdum, luctus urna nec, lacinia odio. Fusce pretium id velit vel tempus. Ut convallis mauris suscipit</p>
  <h2 class="abs band-title">Professionelle Immobilienbewertung</h2>
</section>

<section>
  <h2 class="abs services-title">Rundum Sorglos Vertrieb Ihrer Immobilie.</h2>
  <div class="abs svc-back"></div>
  <div class="abs svc-icon-box">
    <svg width="194" height="262" viewBox="0 0 194 262" fill="none" stroke="#fff" stroke-width="3" stroke-linejoin="round">
      <path d="M40 150 L97 67 L154 150"/>
      <path d="M52 68 h14 v20"/>
      <path d="M52 68 v35"/>
      <path d="M50 142 V188 H144 V142"/>
      <path d="M42 194 H152"/>
      <path d="M80 123 L97 100 L114 123 Z"/>
      <path d="M86 188 V158 H108 V188"/>
      <rect x="60" y="160" width="16" height="14"/>
      <rect x="118" y="160" width="16" height="14"/>
    </svg>
  </div>
  <div class="abs svc-card active">
    <h3>Objektaufnahme</h3>
    <p>Detaillierte Einwertung, Preisfindung, Vermessung und Fotografie Ihrer Immobilie.</p>
  </div>
  <div class="abs svc-card muted">
    <h3>Vermarktung</h3>
    <p>Gemeinsame Festlegung eines Vermarktungs- &amp; Präsentationskonzeptes für Ihre Immobilie.</p>
  </div>
  <div class="abs slider-arrow" style="left:76px">&lt;</div>
  <div class="abs slider-arrow" style="left:1086px">&gt;</div>
</section>

<svg class="abs key-band" viewBox="0 0 1200 145" width="1200" height="145" role="img" aria-label="Foto eines Schlüssels im Türschloss vor grünem Hintergrund">
  <defs>
    <linearGradient id="keyTone" x1="0" y1="0" x2="1" y2="0">
      <stop offset="0" stop-color="#6e9a3c"/>
      <stop offset=".5" stop-color="#a9c470"/>
      <stop offset=".7" stop-color="#5c5a4a"/>
      <stop offset="1" stop-color="#7a4b2a"/>
    </linearGradient>
  </defs>
  <path d="M0 0 H1200 V110 Q600 118 500 143 Q250 112 0 110 Z" fill="url(#keyTone)"/>
</svg>

<section>
  <h2 class="abs quote-title">Das sagen unsere Kunden</h2>
  <svg class="abs quote-mark" width="108" height="82" viewBox="0 0 108 82" fill="#7b7c84">
    <path d="M0 0 H46 V40 Q46 70 18 82 L12 72 Q26 62 26 48 H0 Z"/>
    <path d="M60 0 H106 V40 Q106 70 78 82 L72 72 Q86 62 86 48 H60 Z"/>
  </svg>
  <p class="abs quote-text">Ich würde Herrn Brunkhag als freundlich, zuverlässig und integer beschreiben. Eigenschaften, die in dieser Kombination nicht branchentypisch sind. Er hat uns beim Erwerb einer Eigentumswohnung sehr kompetent beraten und bis zum Abschluss herausragend begleitet. Ich kann die "Tilo Brunkhag Immobilienberatung" wirklich uneingeschränkt empfehlen.</p>
  <svg class="abs portrait" viewBox="0 1810 1200 470" width="1200" height="470">
    <defs>
      <linearGradient id="portraitTone" x1="0" y1="0" x2="1" y2="0">
        <stop offset="0" stop-color="#0c0c0c"/>
        <stop offset=".6" stop-color="#3a3a3a"/>
        <stop offset="1" stop-color="#8a8a8a"/>
      </linearGradient>
    </defs>
    <polygon points="799,2048 1200,1815 1200,2275" fill="url(#portraitTone)" role="img" aria-label="Schwarzweiß-Porträt eines lächelnden Kunden"/>
  </svg>
</section>

<section>
  <div class="abs contact-bar">
    <svg width="52" height="38" viewBox="0 0 52 38" style="position:absolute;left:18px;top:9px" fill="none" stroke="#fff" stroke-width="2.5">
      <rect x="2" y="2" width="48" height="34"/>
      <path d="M2 2 L26 22 L50 2 M2 36 L20 18 M50 36 L32 18"/>
    </svg>
  </div>
  <svg class="abs contact-map" viewBox="0 0 1118 145" width="1118" height="145" role="img" aria-label="Stadtplan mit Lage des Büros">
    <defs>
      <linearGradient id="mapTone" x1="0" y1="0" x2="1" y2="0">
        <stop offset="0" stop-color="#a9c8ef"/>
        <stop offset=".45" stop-color="#d8dcd2"/>
        <stop offset="1" stop-color="#e6e3dc"/>
      </linearGradient>
    </defs>
    <path d="M0 0 H1118 V95 Q700 100 400 145 Q200 95 0 95 Z" fill="url(#mapTone)"/>
  </svg>
  <h2 class="abs contact-title">Treten Sie mit Uns in Kontakt.</h2>

  <div class="abs contact-item" style="top:2644px">
    <svg viewBox="0 0 46 46" height="46" fill="none" stroke="#3a4160" stroke-width="2">
      <rect x="8" y="4" width="20" height="40"/><rect x="28" y="18" width="12" height="26"/>
      <path d="M12 10h4M20 10h4M12 17h4M20 17h4M12 24h4M20 24h4M12 31h4M20 31h4M31 25h6M31 32h6M16 44v-6h4v6"/>
    </svg>
    <span>Lindenhofweg 12<br>90402 Nürnberg</span>
  </div>
  <div class="abs contact-item" style="top:2738px">
    <svg viewBox="0 0 46 46" height="46" fill="none" stroke="#3a4160" stroke-width="2">
      <path d="M10 4 L18 14 L13 20 Q18 30 27 34 L33 28 L43 36 L37 43 Q20 42 6 22 Q3 12 10 4 Z"/>
    </svg>
    <span>+49 911 5550 21 40</span>
  </div>
  <div class="abs contact-item" style="top:2826px">
    <svg viewBox="0 0 46 46" height="46" fill="none" stroke="#3a4160" stroke-width="2">
      <rect x="13" y="2" width="20" height="42" rx="3"/><path d="M13 9h20M13 36h20M21 40h4"/>
    </svg>
    <span>+49 176 5550 73 28</span>
  </div>
  <div class="abs contact-item" style="top:2909px">
    <svg viewBox="0 0 46 46" height="46" fill="none" stroke="#3a4160" stroke-width="2">
      <rect x="2" y="10" width="42" height="28"/><path d="M2 10 L23 27 L44 10 M2 38 L18 23 M44 38 L28 23"/>
    </svg>
    <span>tb@giebelhaus-immo.de</span>
  </div>

  <div class="abs field" style="left:530px;top:2650px;width:268px">Ihr Name*</div>
  <div class="abs field" style="left:837px;top:2650px;width:268px">Straße, Hausnummer*</div>
  <div class="abs field" style="left:530px;top:2702px;width:268px">E-Mail*</div>
  <div class="abs field" style="left:837px;top:2702px;width:268px">Postleitzahl, Ort*</div>
  <div class="abs field message" style="left:530px;top:2762px;width:575px">Ihre Nachricht an Uns.</div>
</section>

<footer class="abs footer">
  <a style="left:484px">Impressum</a>
  <a style="left:621px">Datenschutz</a>
</footer>

</body>
</html>
```